"Steady Frame Slim Down Roadmap" eBook cover

THE TITLE HAS CHANGED SLIGHTLY TO ;
"Steady Frame Slim Down Roadmap"

The following is for a fat loss, health and fitness eBook titled "Steady Frame Slim Down Roadmap." This design should help promote and market this product, as well as intrigue those to not only make a purchase... but want to very much participate in the material and follow the material!

There is no restriction of color, idea, etc. PLEASE help me with your expertise in developing a great cover for this project...

THANKS SO MUCH

This book separates others just by the quality information provided. To much trial and error is wasted on false claims and overrated programs....I have provided the books topics below to hopefully give you a better understanding;
CHAPTER 1
Steady Frame Slimdown Manual
- What is it?
- Why it works?
- Why it will work for you?
CHAPTER 2
Kill Cardio
- Why cardio sucks?
- Myth about cardio?
- What cardio works for fat loss
CHAPTER 3
Iron vs. Machine
- What type of resistance training is best for fat loss?
- Why?
- The big pitfall to working on machines?
CHAPTER 4
Should You Really Eat That?
- Foods that build muscle
- Foods that burn fat
- Foods that suck!
CHAPTER 5
Playing With Iron
- Playing with iron
- 17 upper body builders
- 17 lower body builders
- 11 workouts in 11 minutes
CHAPTER 6
Buying Equipment On A Budget
- How to find dirt cheap dumbbells?
- How to build equipment under $100

THANKS AGAIN!

Target Market(s)

Self-Help / Health And Fitness / Nutrition

Industry/Entity Type

Health And Wellness

Font styles to use
Serif
Sans Serif
Other font styles liked:
• Tahoma, Verdana, Calibri

Requirements
Must have
• MUST MEET NORVEXA.example GUIDLINES ;
• File Types
• Lumira Author Hub currently accepts two types of files for cover images:
• JPEG (JPEG / JPG)
• TIFF (TIF / TIFF)
• We apply additional compression to images when displaying them on the website. For best results, please upload your images with minimal compression.
• Dimensions
• Requirements for the size of your cover art must have an ideal height/width ratio of at least 8:5 (1.6), meaning:
• • A minimum of 625 pixels on the shortest side and 1000 pixels on the longest side
• • For best quality, your image should be 2500 pixels on the longest side
• Important: We cannot accept any images larger than 10,000 pixels on the longest side.
• Size
• Your cover image must be less than 50MB. If the file type you are using supports compression, make sure to enable as little compression as possible, e.g. none for TIFF. Be sure to save your file with 72 dots per inch (DPI).
• Color
• Product images display on the Norvexa website using the RGB (red, green, blue) color mode or profile. RGB is the color mode native to the web and many color screen displays, as these three colors displayed at varying levels of intensity create over 16 million colors. When saving and uploading your cover image file, save your file ONLY as RGB - not CMYK or sRGB- for the color profile. You can usually find this option in the File saving dialog of image manipulation programs such as Photoshop.
• Some programs may also refer to RGB color as 'True Color' in some programs. If in doubt, try opening a JPG inside Internet Explorer, Firefox, or Safari. If a JPG opens fine inside a web browser, it's most likely okay to use as a cover image.
• Make sure to save your image without color separation. This is usually a pre-press or color palette option. Use your image manipulation program or image analysis tool (some are available free online) to verify that your image file doesn't have color separation.
• Use color images whenever possible and relevant. In addition to the Lumira black and white Z Slate reading devices, customers can read your books on full color Tessel devices and free Lumira reading apps for iPhone, iPad, Android, PC or Mac.
Should not have
• NO MALE OR FEMALE MODLES OR HALF NAKED PEOPLE...

```html
<!DOCTYPE html>
<html lang="en">
<head>
<meta charset="utf-8">
<title>Steady Frame Slim Down Roadmap – eBook Cover</title>
<link href="https://fonts.googleapis.com/css2?family=Oswald:wght@200;300;600;700&display=swap" rel="stylesheet">
<style>
  :root {
    --navy: #1b315d;
    --grid-line: rgba(88, 130, 200, 0.22);
    --grid-line-soft: rgba(88, 130, 200, 0.10);
    --title-blue: #2e69c2;
    --figure-red: rgba(184, 41, 61, 0.55);
    --figure-red-fade: rgba(184, 41, 61, 0);
    --figure-green: rgba(46, 156, 112, 0.55);
    --figure-green-fade: rgba(46, 156, 112, 0);
  }

  * { margin: 0; padding: 0; box-sizing: border-box; }

  html, body {
    width: 846px;
    height: 1200px;
    overflow: hidden;
  }

  .cover {
    position: relative;
    width: 846px;
    height: 1200px;
    background-color: var(--navy);
    background-image:
      linear-gradient(var(--grid-line) 1px, transparent 1px),
      linear-gradient(90deg, var(--grid-line) 1px, transparent 1px),
      linear-gradient(var(--grid-line-soft) 1px, transparent 1px),
      linear-gradient(90deg, var(--grid-line-soft) 1px, transparent 1px);
    background-size: 98px 98px, 98px 98px, 49px 49px, 49px 49px;
    font-family: "Oswald", "Arial Narrow", sans-serif;
    color: var(--title-blue);
    text-transform: uppercase;
  }

  .cover__title { font-weight: inherit; }

  .cover__line {
    position: absolute;
    left: 0;
    width: 100%;
    text-align: center;
    white-space: nowrap;
    line-height: 1;
  }

  .title-strong {
    font-weight: 700;
    font-size: 158px;
    letter-spacing: 0.10em;
    padding-left: 0.10em;
  }

  .title-strong--first { top: 88px; }
  .title-strong--second { top: 238px; letter-spacing: 0.06em; padding-left: 0.06em; }

  .title-light {
    top: 440px;
    font-weight: 200;
    font-size: 100px;
    letter-spacing: 0.10em;
    padding-left: 0.10em;
  }

  .figures {
    position: absolute;
    left: 170px;
    top: 560px;
    width: 500px;
    height: 300px;
    background:
      radial-gradient(ellipse 95px 150px at 26% 50%, var(--figure-red) 0%, var(--figure-red-fade) 100%),
      radial-gradient(ellipse 130px 150px at 74% 50%, var(--figure-green) 0%, var(--figure-green-fade) 100%);
  }

  .title-bottom {
    top: 890px;
    font-weight: 700;
    font-size: 94px;
    letter-spacing: 0.24em;
    padding-left: 0.24em;
  }

  .author {
    top: 1054px;
    font-weight: 600;
    font-size: 44px;
    letter-spacing: 0.08em;
    padding-left: 0.08em;
  }
</style>
</head>
<body>
  <main class="cover">
    <h1 class="cover__title">
      <span class="cover__line title-strong title-strong--first">Steady</span>
      <span class="cover__line title-strong title-strong--second">Frame</span>
      <span class="cover__line title-light">Slim Down</span>
      <span class="cover__line title-bottom">Roadmap</span>
    </h1>
    <div class="figures" role="img" aria-label="Outline illustration: a heavier red figure beside a slimmer green figure with raised arms"></div>
    <p class="cover__line author">Author's Name</p>
  </main>
</body>
</html>
```